Redesign of a Brochure based on an exsiting example for Web download and email marketing

Can you create a professional brochure based on the attached PDF. We need to keep the name, the logo and the content but everything else can be changed . The PDF will primarily be will be used for web download and email marking but it aslo be printed out for a poster design will be appropriate

Target Market(s)

Business to Business

Industry/Entity Type

Marketing

Font styles to use
Serif

Requirements
Must have
• Must have the existing logo ( in the attached document) and contain the same content

```html
<!DOCTYPE html>
<html lang="en">
<head>
<meta charset="utf-8">
<title>IT View – Technology Towers Brochure Spread</title>
<link rel="stylesheet" href="https://fonts.googleapis.com/css2?family=Tinos:wght@400;700&display=swap">
<style>
  :root {
    --stage: #454545;
    --paper: #ffffff;
    --navy: #1a3e74;
    --navy-deep: #242a63;
    --heading: #1b3a6b;
    --tab-blue: #4a88c7;
    --ink: #2b2b2b;
    --sky-light: #dfeaf4;
    --sky-mid: #7aa6cf;
    --glass: #3f6f9c;
  }
  * { box-sizing: border-box; margin: 0; padding: 0; }
  html, body { width: 1200px; height: 1200px; overflow: hidden; background: var(--stage); }
  body { position: relative; font-family: "Tinos", "Times New Roman", serif; color: var(--ink); }

  .spread {
    position: absolute; left: 20px; top: 178px;
    width: 1195px; height: 868px;
    transform: scale(0.9707); transform-origin: 0 0;
    background: var(--paper);
  }
  .page { position: absolute; top: 0; height: 868px; overflow: hidden; }
  .page--left { left: 0; width: 599px; }
  .page--right { left: 599px; width: 596px; border-left: 1px solid #e4e4e4; }

  .hero-photo {
    position: absolute; left: 0; top: 0; width: 599px; height: 390px;
    background: linear-gradient(160deg, var(--sky-light) 0%, var(--sky-mid) 45%, var(--glass) 100%);
    clip-path: polygon(0 0, 100% 0, 100% 388px, 125px 289px, 0 372px);
  }
  .title { position: absolute; left: 33px; top: 362px; font-size: 50px; font-weight: 400; color: var(--heading); line-height: 1; }
  .subtitle { position: absolute; left: 33px; top: 421px; font-size: 27px; font-weight: 400; color: var(--heading); line-height: 1; }

  .body-copy { font-size: 14.2px; line-height: 17px; text-align: justify; }
  .body-copy p + p { margin-top: 13px; }
  .intro { position: absolute; left: 33px; top: 461px; width: 532px; }
  .drop-cap { float: left; font-size: 62px; line-height: 50px; margin: 2px 6px 0 0; color: #222; }

  .sources-band { position: absolute; left: 0; top: 746px; width: 599px; height: 122px; background: var(--navy); color: #fff; }
  .sources-label { position: absolute; left: 110px; top: 24px; font-size: 33px; line-height: 28px; }
  .sources-rule { position: absolute; left: 229px; top: 29px; width: 1px; height: 52px; background: #fff; }
  .sources-list { position: absolute; left: 241px; top: 27px; list-style: none; font-size: 14.5px; line-height: 17px; }

  .section-title { position: absolute; left: 0; width: 596px; top: 26px; text-align: center; font-size: 31px; font-weight: 700; color: var(--heading); }
  .ribbon { position: absolute; top: 96px; width: 215px; height: 64px; }
  .ribbon--measure { left: 42px; top: 98px; }
  .ribbon--insight { left: 328px; }
  .ribbon-text { position: absolute; top: 1px; left: 55px; font-size: 26px; font-weight: 700; color: #fff; }

  .metric { position: absolute; left: 40px; width: 519px; }
  .metric--datacentre { top: 211px; }
  .metric--compute { top: 559px; }
  .metric-tag {
    float: left; width: 266px; height: 90px; margin: -16px 16px 0 -7px;
    shape-outside: inset(0 0 6px 0);
  }
  .metric-tag-box {
    width: 256px; height: 74px; padding: 12px 0 0 12px;
    background: var(--tab-blue); color: #fff;
    font-weight: 700; font-size: 14.2px; line-height: 17px; letter-spacing: 0.2px;
    clip-path: polygon(0 0, 222px 0, 100% 30px, 100% 100%, 0 100%);
  }
  .metric--compute .metric-tag { height: 82px; margin-top: -14px; }
  .metric--compute .metric-tag-box { height: 75px; padding-top: 4px; }
  .metric-note { margin-top: 15px; }

  .measure-band { position: absolute; left: 0; bottom: 0; width: 596px; height: 122px; }
</style>
</head>
<body>
  <main class="spread">
    <section class="page page--left">
      <div class="hero-photo" role="img" aria-label="Photograph of modern glass office towers beneath a streaked blue sky"></div>
      <h1 class="title">IT view</h1>
      <h2 class="subtitle">Technology Towers and Sub Towers</h2>
      <div class="intro body-copy">
        <p><span class="drop-cap">T</span>he Technology Towers layer captures the cost of the technologies, services and platforms that underpin IT products &amp; Services. A few of these categories, such as telephony, can be charged directly back to the business. However, the vast majority of these towers are shared between products and services. Typically this is infrastructure and as this usually represents 60% to 70% of all IT expenditure it is a good place to optimise costs.</p>
        <p>The key is to create transparency, establish Price for Performance measures and challenge technology leaders and vendors to find efficiencies to reduce these cost every year.</p>
        <p>In this model we have made a conscious effort to keep this layer as simple as possible, that is, to capture the most useful and significant data for the least amount of effort. This approach is shown in the sample output opposite.</p>
        <p>In this model we have made a conscious effort to keep this layer as simple as possible, that is, to capture the most useful and significant data for the least amount of effort. This approach is shown in the sample output opposite.</p>
      </div>
      <footer class="sources-band">
        <div class="sources-label">Data<br>sources</div>
        <div class="sources-rule"></div>
        <ol class="sources-list">
          <li>1. Layer 1 - IT Costs Centres - Run</li>
          <li>2. Budget and Time Recording Systems</li>
          <li>3. Configuration Management Databases</li>
        </ol>
      </footer>
    </section>

    <section class="page page--right">
      <h2 class="section-title">Sample Output</h2>

      <div class="ribbon ribbon--measure">
        <svg width="215" height="64" viewBox="0 0 215 64">
          <defs>
            <linearGradient id="ribbonFill" x1="0" y1="0" x2="1" y2="0">
              <stop offset="0" stop-color="#4d8fd0"/>
              <stop offset="0.45" stop-color="#2a3f86"/>
              <stop offset="1" stop-color="#242a63"/>
            </linearGradient>
          </defs>
          <polygon points="30,0 212,0 203,35 0,35 " fill="url(#ribbonFill)"/>
          <polygon points="0,35 30,35 30,45 20,60" fill="#3d78bd"/>
        </svg>
        <span class="ribbon-text">Measure</span>
      </div>
      <div class="ribbon ribbon--insight">
        <svg width="215" height="64" viewBox="0 0 215 64">
          <polygon points="30,0 212,0 203,35 0,35" fill="url(#ribbonFill)"/>
          <polygon points="0,35 30,35 30,45 20,60" fill="#3d78bd"/>
        </svg>
        <span class="ribbon-text">Insight</span>
      </div>

      <article class="metric metric--datacentre body-copy">
        <div class="metric-tag"><div class="metric-tag-box">Datacentre<br>Owned Datacentre Cost per Rack<br>Co-location Datacentre Cost</div></div>
        <p>Co-located datacentre costs are usually charged inclusively on a per rack basis. These costs include physical hosting and electricity costs per machine. Here we use this measure to compare the costs of in-house datacentres against each other and external hosted suppliers. In this model, datacentre costs are modelled with four categories: Electricity, Equipment, Support and Buildings/Rent. Electricity costs are typically 20% of datacentre costs but this number can vary greatly. All datacentre equipment, racks, cooling fire suppression etc. is captured in the Equipment category and it is important that any depreciation costs are normalised using the model standard.</p>
        <p class="metric-note">The results can be used for demand management, charge-back, and although it does not give exact details on how to optimise datacentres, it does give you very good pointers where to start. When drilling down into the costs it is important to add technical, performance and utilisation data for each datacentre. For example, servers per datacentre, what type, unused capacity and where the equipment is in the depreciation cycle.</p>
      </article>

      <article class="metric metric--compute body-copy">
        <div class="metric-tag"><div class="metric-tag-box">X86 Compute<br>CPU cost Per Owned Datacentre<br>CPU cost Co-Location Datacentre<br>CPU cost per Cloud CPU</div></div>
        <p>The X86 CPU measure is used for comparing the fully loaded cost of running X86 compute in-house, in co-located data centres and in the cloud. For example, in-house X86 CPU is calculated by dividing the platform costs by the number of X86 CPUs. You should make a discount for any other types of computing power in the datacentre. The in-house X86 category includes costs of Hardware, Software, Maintenance and Support. When examining these figures it is important to capture average unitisation rates as datacentres are often full of old and under-utilised servers.</p>
      </article>

      <svg class="measure-band" viewBox="0 0 596 122" aria-hidden="true">
        <polygon points="0,0 116,98 596,1 596,122 0,122" fill="#1a3e74"/>
        <g fill="none" stroke="#fff" stroke-width="2.4">
          <path d="M515,31 a6,6 0 0 1 12,0 v34 a11,11 0 1 1 -12,0 z"/>
          <circle cx="521" cy="74" r="5" fill="#fff"/>
          <line x1="521" y1="46" x2="521" y2="70"/>
        </g>
        <g stroke="#fff" stroke-width="1.4">
          <line x1="503" y1="37" x2="511" y2="37"/><line x1="503" y1="43" x2="511" y2="43"/>
          <line x1="503" y1="49" x2="511" y2="49"/><line x1="503" y1="55" x2="511" y2="55"/>
          <line x1="531" y1="37" x2="539" y2="37"/><line x1="531" y1="43" x2="539" y2="43"/>
          <line x1="531" y1="49" x2="539" y2="49"/><line x1="531" y1="55" x2="539" y2="55"/>
        </g>
      </svg>
    </section>
  </main>
</body>
</html>
```